Business Card & Stationary Design Project

We are looking for some creative direction for business cards and our stationary.

We are a global logistics firm that has recently changed its name to Marrick Global Logistics and we have a new website due out tomorrow (www.marrick.com.au).

The colours of the company are rich navy tones, I would like to have business cards that fit together to make one picture on the back (possibly an old map of the world??), and the front to be modern contemporary looking.

But I am open to suggestions, so just incorporate our new logo and get going!
Updates

Hi Everyone,

Thank you for all of your designs so far and the time you have put into it.

I have asked many of you for amendments to see if we can get a final product, so with this in mind I am extending the deadline by a few days.

Good luck and thank you once again.

Please message me direct if you need any clarification.

Kind Regards
Colin

Reason: As outlined the extra 3 days is for amendments and changes to the current submissions. Thanks Colin

Industry/Entity Type

Business

```html
<!DOCTYPE html>
<html lang="en">
<head>
<meta charset="utf-8">
<title>Marrick Global Logistics – Stationery</title>
<link rel="stylesheet" href="https://fonts.googleapis.com/css2?family=Questrial&display=swap">
<style>
  :root{
    --navy:#1b3a63;
    --navy-deep:#132c4f;
    --navy-soft:#2a4f82;
    --sky:#3d8fd6;
    --paper:#f4f5f7;
    --ink:#2b2f36;
    --ink-soft:#5b6470;
    --backdrop:#d9dbde;
    --map:rgba(90,130,180,.28);
  }
  *{box-sizing:border-box;margin:0;padding:0}
  html,body{width:1200px;height:899px;overflow:hidden}
  body{background:var(--backdrop);font-family:"Questrial",sans-serif;color:var(--ink);position:relative}
  .piece{position:absolute;overflow:hidden}
  .paper{background:var(--paper);box-shadow:0 2px 6px rgba(0,0,0,.18)}
  .navy{background:linear-gradient(160deg,var(--navy-soft) 0%,var(--navy) 45%,var(--navy-deep) 100%);box-shadow:0 2px 6px rgba(0,0,0,.25)}

  /* company name, set as plain text */
  .company-name{position:absolute;font-family:"Questrial",sans-serif;font-weight:400;line-height:1;white-space:nowrap}
  .company-name--dark{color:var(--navy)}
  .company-name--light{color:#e9eef5}

  .map{position:absolute;border-radius:40%;background:radial-gradient(ellipse at 50% 50%,var(--map) 0%,rgba(90,130,180,.12) 55%,transparent 75%)}

  /* letterhead */
  .letterhead{left:232px;top:108px;width:335px;height:475px}
  .letterhead .company-name{left:0;width:100%;text-align:center;top:42px;font-size:14px}
  .letter-body{position:absolute;left:48px;top:158px;width:252px;font-size:6.2px;line-height:8.2px;color:var(--ink);text-align:justify}
  .letter-body p{margin-bottom:7px}
  .signature{position:absolute;left:48px;top:363px;width:86px;height:14px;background:linear-gradient(90deg,rgba(40,60,200,.18),rgba(40,60,200,.05));border-radius:6px}
  .sign-role{position:absolute;left:48px;top:380px;font-size:6.5px;color:var(--ink)}
  .footer-band{position:absolute;left:0;bottom:0;width:100%;height:20px;background:var(--navy);display:flex;align-items:center;justify-content:space-between;padding:0 10px 0 16px;font-size:5.4px;color:#d8e0ea}
  .footer-band .label{color:var(--sky)}
  .footer-band svg{position:absolute;left:262px;top:0}

  /* folder */
  .folder{left:627px;top:87px;width:394px;height:499px}
  .folder .map{left:30px;top:60px;width:350px;height:360px}
  .folder .company-name{left:0;width:100%;text-align:center;top:246px;font-size:20px}
  .folder__url{position:absolute;left:0;width:100%;top:466px;text-align:center;font-size:10px;color:#c9d4e2}

  /* business cards */
  .card{width:151px;height:86px}
  .card--front{left:112px;top:625px}
  .card--back{left:112px;top:734px;height:87px}
  .card--front .company-name{left:9px;top:14px;font-size:10px}
  .card__person{position:absolute;left:9px;top:38px;font-size:6.3px;color:var(--ink);line-height:7px}
  .card__person .role{font-size:4px;color:var(--ink-soft)}
  .card__contact{position:absolute;left:9px;top:54px;font-size:3.8px;line-height:5px;color:var(--ink-soft);display:grid;grid-template-columns:auto auto;column-gap:10px}
  .card__contact .label{color:var(--sky)}
  .card__band{position:absolute;left:0;bottom:0;width:100%;height:9px;background:var(--navy);font-size:4px;color:#d8e0ea;padding:2px 8px}
  .card--back .map{left:5px;top:5px;width:140px;height:70px}
  .card--back .company-name{left:0;width:100%;text-align:center;top:38px;font-size:9px}
  .card__url{position:absolute;left:0;width:100%;top:76px;text-align:center;font-size:4px;color:#c9d4e2}

  /* envelopes */
  .envelope{top:637px;width:375px;height:178px}
  .envelope--front{left:303px}
  .envelope--front .company-name{left:16px;top:30px;font-size:14px}
  .envelope__address{position:absolute;left:16px;top:150px;font-size:5.6px;line-height:6.4px;color:var(--navy)}
  .envelope__address .url{color:var(--sky)}
  .envelope--back{left:714px}
  .envelope--back svg{position:absolute;left:0;top:0}
</style>
</head>
<body>

<section class="piece paper letterhead" aria-label="Letterhead">
  <div class="company-name company-name--dark">Marrick Global Logistics</div>
  <div class="letter-body">
    <p>Letterhead samples are a great way of deciding what kind of letterhead you want to design for you and your company. The internet has a ton of great letterhead samples to browse through. Whether you want something simple, with just a couple lines of text of your business information, or something decorative and stunning, with photos and logos on the top and bottom of the page, it will be easy to find what you want, because there are samples online for basically any type of letterhead you could want.</p>
    <p>Any business could easily benefit from browsing through some letterhead samples, if only to get an idea for what kind of letterhead their company might want. Letterheads are just one of the tools that a business professional could use to help increase their customer base, and to really be memorable to everyone they write a letter to. Letterhead is quite an effective tool for marketing and advertising, but because it's such a simple and well known idea, it is often unfairly overlooked. Make sure you don't make that mistake, and make some letterhead samples of your own today.</p>
    <p>Whether you want to get new customers to remember you and become part of your clientele, or you just want to send out friendly reminders to your existing clients, customizing your own letterhead samples can really help you out. Try out some letterhead samples and you will not regret it, and I'm sure you will add a new tool to your business' arsenal of networking, marketing, and advertising tools.</p>
  </div>
  <div class="signature" role="img" aria-label="Handwritten signature of Daniel Whitcombe"></div>
  <div class="sign-role">company director</div>
  <div class="footer-band">
    <span>58 Harbour Lane Pyrmont NSW 2009 &nbsp;<span class="label">Phone:</span> 02 9100 4200 &nbsp;<span class="label">Fax:</span> 02 9100 4201</span>
    <span>www.marrick.com.au</span>
    <svg width="20" height="20" viewBox="0 0 20 20" aria-hidden="true"><line x1="2" y1="20" x2="20" y2="2" stroke="var(--sky)" stroke-width="1"/></svg>
  </div>
</section>

<section class="piece navy folder" aria-label="Presentation folder">
  <div class="map" role="img" aria-label="Faint world map in navy tones"></div>
  <div class="company-name company-name--light">Marrick Global Logistics</div>
  <div class="folder__url">www.marrick.com.au</div>
</section>

<section class="piece paper card card--front" aria-label="Business card front">
  <div class="company-name company-name--dark">Marrick Global Logistics</div>
  <div class="card__person">COLIN BARLOW<br><span class="role">General Manager</span></div>
  <div class="card__contact">
    <span><span class="label">Phone:</span> 02 9100 4200</span><span><span class="label">Fax:</span> 02 9100 4201</span>
    <span><span class="label">Mobile:</span> 0400 123 456</span><span><span class="label">Email:</span> colin@marrick.com.au</span>
    <span>linkedin.com/colin-barlow</span><span></span>
  </div>
  <div class="card__band">58 Harbour Lane Pyrmont NSW 2009</div>
</section>

<section class="piece navy card card--back" aria-label="Business card back">
  <div class="map" role="img" aria-label="Faint world map in navy tones"></div>
  <div class="company-name company-name--light">Marrick Global Logistics</div>
  <div class="card__url">www.marrick.com.au</div>
</section>

<section class="piece paper envelope envelope--front" aria-label="Envelope front">
  <div class="company-name company-name--dark">Marrick Global Logistics</div>
  <div class="envelope__address">58 Harbour Lane<br>Pyrmont NSW 2009<br><span class="url">www.marrick.com.au</span></div>
</section>

<section class="piece paper envelope envelope--back" aria-label="Envelope back">
  <svg width="375" height="70" viewBox="0 0 375 70" aria-hidden="true">
    <path d="M0 0 H375 V48 Q375 62 355 62 H20 Q0 62 0 48 Z" fill="var(--navy)"/>
  </svg>
</section>

</body>
</html>
```